Criação de Papelaria Profissional para Crianças & Infantil
A empresa queria:
" Esta empresa preza por vender roupas de altíssima qualidade e marcas diferenciadas, a fim de encantar pais e filhos, garantindo conforto e estilo aos pequenos. "

```html
<!DOCTYPE html>
<html lang="pt-BR">
<head>
<meta charset="UTF-8">
<title>Lumiri — Cartão Fidelidade</title>
<link rel="stylesheet" href="https://fonts.googleapis.com/css2?family=Poppins:wght@400;500;600;700&display=swap">
<style>
  :root {
    --bg: #6a2e86;
    --card-back: #6f3190;
    --white: #ffffff;
    --purple-dark: #6a3a8c;
    --purple-soft: #9a6fc0;
    --logo: #9b76c8;
    --band-blue: #8fc6e4;
    --band-pink: #e58ba4;
    --band-yellow: #f4c15f;
    --band-teal: #9ed8c8;
    --star: #ef8a88;
    --accent: #f6c35c;
    --faint: rgba(190, 150, 230, 0.28);
  }
  * { margin: 0; padding: 0; box-sizing: border-box; }
  html, body { width: 1200px; height: 1200px; overflow: hidden; }
  body {
    background: var(--bg);
    font-family: "Poppins", sans-serif;
    position: relative;
  }
  .card {
    position: absolute;
    left: 192px;
    width: 816px;
    border-radius: 48px;
    overflow: hidden;
    box-shadow: 0 18px 40px rgba(40, 10, 60, 0.35);
  }
  .card-front {
    top: 137px;
    height: 451px;
    background: var(--white);
  }
  .card-title {
    position: absolute;
    top: 30px;
    width: 100%;
    text-align: center;
    font-size: 30px;
    letter-spacing: 2px;
    font-weight: 600;
    color: var(--purple-dark);
  }
  .card-title strong { color: var(--purple-soft); font-weight: 700; }
  .brand {
    position: absolute;
    top: 148px;
    width: 100%;
    display: flex;
    justify-content: center;
    align-items: center;
    gap: 18px;
  }
  .brand-dot {
    width: 40px; height: 40px;
    border-radius: 50%;
    background: var(--band-pink);
  }
  .brand-name {
    font-size: 100px;
    font-weight: 600;
    line-height: 1;
    color: var(--logo);
  }
  .tagline {
    position: absolute;
    top: 276px;
    left: 0;
    width: 600px;
    text-align: right;
    font-size: 18px;
    font-weight: 500;
    color: var(--purple-dark);
  }
  .color-band {
    position: absolute;
    bottom: 0; left: 0;
    width: 100%; height: 22px;
    display: flex;
  }
  .color-band span { flex: 1; }
  .color-band .blue { background: var(--band-blue); }
  .color-band .pink { background: var(--band-pink); }
  .color-band .yellow { background: var(--band-yellow); }
  .color-band .teal { background: var(--band-teal); }

  .card-back {
    top: 607px;
    height: 456px;
    background: var(--card-back);
  }
  .reward-text {
    position: absolute;
    top: 30px;
    width: 100%;
    text-align: center;
    font-size: 26px;
    line-height: 37px;
    font-weight: 600;
    color: var(--white);
  }
  .reward-text em { font-style: normal; color: var(--accent); }
  .faint-mark {
    position: absolute;
    left: -60px; top: 120px;
    width: 230px; height: 230px;
    border-radius: 50%;
    background: var(--faint);
  }
  .stamps {
    position: absolute;
    left: 276px;
    top: 134px;
    display: grid;
    grid-template-columns: repeat(4, 96px);
    grid-template-rows: repeat(2, 96px);
    column-gap: 18px;
    row-gap: 12px;
  }
  .stamps svg { width: 96px; height: 96px; }
  .contact {
    position: absolute;
    bottom: 40px;
    width: 100%;
    display: flex;
    justify-content: center;
    align-items: center;
    gap: 16px;
    font-size: 19px;
    font-weight: 500;
    color: var(--white);
  }
  .contact-item { display: flex; align-items: center; gap: 8px; }
  .contact-divider { width: 2px; height: 24px; background: rgba(255,255,255,0.6); }
  .contact svg { width: 20px; height: 20px; }
</style>
</head>
<body>
  <section class="card card-front">
    <h1 class="card-title">CARTÃO <strong>FIDELIDADE</strong></h1>
    <div class="brand">
      <span class="brand-dot"></span>
      <span class="brand-name">Lumiri</span>
    </div>
    <p class="tagline">Conforto para crescer feliz</p>
    <div class="color-band">
      <span class="blue"></span><span class="pink"></span><span class="yellow"></span><span class="teal"></span>
    </div>
  </section>

  <section class="card card-back">
    <p class="reward-text">Complete a cartela e ganhe <em>30%</em><br>de desconto na próxima compra!</p>
    <div class="faint-mark" role="img" aria-label="Marca decorativa suave da loja"></div>
    <svg width="0" height="0" style="position:absolute">
      <defs>
        <path id="stamp-star" d="M50 8 L62 36 L92 38 L69 58 L77 88 L50 72 L23 88 L31 58 L8 38 L38 36 Z"
              fill="var(--star)" stroke="var(--star)" stroke-width="10" stroke-linejoin="round"/>
      </defs>
    </svg>
    <div class="stamps">
      <svg viewBox="0 0 100 100"><use href="#stamp-star"/></svg>
      <svg viewBox="0 0 100 100"><use href="#stamp-star"/></svg>
      <svg viewBox="0 0 100 100"><use href="#stamp-star"/></svg>
      <svg viewBox="0 0 100 100"><use href="#stamp-star"/></svg>
      <svg viewBox="0 0 100 100"><use href="#stamp-star"/></svg>
      <svg viewBox="0 0 100 100"><use href="#stamp-star"/></svg>
      <svg viewBox="0 0 100 100"><use href="#stamp-star"/></svg>
      <svg viewBox="0 0 100 100"><use href="#stamp-star"/></svg>
    </div>
    <div class="contact">
      <span class="contact-item">
        <svg viewBox="0 0 24 24"><path d="M6.6 10.8a15 15 0 0 0 6.6 6.6l2.2-2.2a1 1 0 0 1 1-.25 11.4 11.4 0 0 0 3.6.57 1 1 0 0 1 1 1V20a1 1 0 0 1-1 1A17 17 0 0 1 3 4a1 1 0 0 1 1-1h3.5a1 1 0 0 1 1 1c0 1.25.2 2.45.57 3.6a1 1 0 0 1-.25 1z" fill="#ffffff"/></svg>
        (00) 99999-0000
      </span>
      <span class="contact-divider"></span>
      <span class="contact-item">@lumiri</span>
    </div>
  </section>
</body>
</html>
```